Brindlow tile letterhead contractor

I would like to get a very good expressive letterhead or resume with great 3D design as a tile contractor company offering my services to others tile companies, general contractors and home owners clients. (This is the idea)
Founder/owner.
“Proud to represent and provide my life’s passion services as brindlow tile.”
I’m journeyman setter, I have passion for creating visually stunning designs with a focus on creativity usability. I have been working as setter with a remarkable companies for over 20 years and I specialize in commercial and residential projects.
My experience and expertise have enabled me to create beautiful master pieces for a wide range of clients, from a small businesses to a large corporations.
My first goal in any project that you hire me for is to provide a professional and high-quality product that meets and exceeds your expectations. You can really assured that I will strive tirelessly to produce the best results for our clients until the final project is done.
*My team will move forward with your needs in every step we walk together
*We have a very solid foundations knowledge altogether rely in the best equipment possible to make (builds)what it takes with best quality possible
*I’m an independent contractor and beaten to another prestigious companies …. ETC. ETC.
ILL TRY TO KEEP UPDATING MORE INFO.
General contractors, tile companies and home owners builders
Tile construction

```html
<!DOCTYPE html>
<html lang="en">
<head>
<meta charset="utf-8">
<title>Brindlow Tile – Letterhead and Envelope</title>
<link rel="stylesheet" href="https://fonts.googleapis.com/css2?family=Open+Sans:wght@400;600&display=swap">
<style>
  :root {
    --backdrop: #e9e9ea;
    --paper: #fbfbfb;
    --paper-edge: #dedede;
    --brand: #4b3234;
    --ink: #6b6b6e;
    --ink-soft: #8a8a8d;
    --signature-tone: #c9ccd6;
    --flap-line: #e6e6e6;
  }
  * { box-sizing: border-box; margin: 0; padding: 0; }
  html, body { width: 1200px; height: 795px; overflow: hidden; background: var(--backdrop); }
  body { position: relative; font-family: "Open Sans", sans-serif; color: var(--ink); }

  .letterhead {
    position: absolute; left: 70px; top: 40px;
    width: 505px; height: 714px;
    background: var(--paper);
    box-shadow: 0 1px 0 var(--paper-edge), 0 6px 18px rgba(0,0,0,.08);
    padding: 52px 48px 40px 52px;
  }
  .company-name { display: flex; align-items: center; justify-content: flex-end; gap: 10px; }
  .company-name__square { width: 22px; height: 22px; background: var(--brand); flex: none; }
  .company-name__text {
    font-family: "Open Sans", sans-serif; font-weight: 600; color: var(--brand);
    font-size: 18px; line-height: 1;
  }

  .letter { margin-top: 44px; font-size: 8.6px; line-height: 1.6; color: var(--ink); }
  .letter__greeting { margin-bottom: 8px; color: var(--ink-soft); }
  .letter p { margin-bottom: 9px; text-indent: 18px; }
  .letter__closing { margin-top: 14px; color: var(--ink-soft); }
  .letter__signature { display: block; width: 90px; height: 44px; margin-top: 10px; border-radius: 4px; background: var(--signature-tone); }

  .contact {
    position: absolute; left: 52px; right: 48px; bottom: 44px;
    display: flex; justify-content: space-between; align-items: flex-end;
    font-size: 9.5px; color: var(--ink);
  }
  .contact__group { display: flex; flex-direction: column; gap: 5px; }
  .contact__group--end { align-items: flex-end; }
  .contact__line { display: flex; align-items: center; gap: 6px; }
  .contact__icon { width: 10px; height: 10px; fill: var(--brand); flex: none; }

  .envelope {
    position: absolute; left: 610px; top: 250px;
    width: 540px; height: 270px;
    background: var(--paper);
    box-shadow: 0 1px 0 var(--paper-edge), 0 6px 18px rgba(0,0,0,.08);
  }
  .envelope__flap {
    position: absolute; left: 16px; right: 16px; top: 0; height: 112px;
    border: 1px solid var(--flap-line); border-top: none;
    border-radius: 0 0 12px 12px;
  }
  .envelope .company-name { position: absolute; right: 44px; top: 38px; }
</style>
</head>
<body>

<section class="letterhead">
  <header class="company-name">
    <span class="company-name__square"></span>
    <span class="company-name__text">Brindlow Tile</span>
  </header>

  <div class="letter">
    <div class="letter__greeting">Dear customer,</div>
    <p>Lorem ipsum dolor sit amet, consectetur adipisicing elit, sed do eiusmod tempor incididunt ut labore et dolore magna aliqua. Ut enim ad minim veniam, quis nostrud exercitation ullamco laboris nisi ut aliquip ex ea commodo consequat. Duis aute irure dolor in reprehenderit in voluptate velit esse cillum dolore eu fugiat nulla pariatur. Excepteur sint occaecat cupidatat non proident, sunt in culpa qui officia deserunt mollit anim id est laborum.</p>
    <p>Lorem ipsum dolor sit amet, consectetur adipisicing elit, sed do eiusmod tempor incididunt ut labore et dolore magna aliqua. Ut enim ad minim veniam, quis nostrud exercitation ullamco laboris nisi ut aliquip ex ea commodo consequat. Duis aute irure dolor in reprehenderit in voluptate velit esse cillum dolore eu fugiat nulla pariatur. Excepteur sint occaecat cupidatat non proident, sunt in culpa qui officia deserunt mollit anim id est laborum.</p>
    <p>Lorem ipsum dolor sit amet, consectetur adipisicing elit, sed do eiusmod tempor incididunt ut labore et dolore magna aliqua. Ut enim ad minim veniam, quis nostrud exercitation ullamco laboris nisi ut aliquip ex ea commodo consequat. Duis aute irure dolor in reprehenderit in voluptate velit esse cillum dolore eu fugiat nulla pariatur. Excepteur sint occaecat cupidatat non proident, sunt in culpa qui officia deserunt mollit anim id est laborum.</p>
    <p>Lorem ipsum dolor sit amet, consectetur adipisicing elit, sed do eiusmod tempor incididunt ut labore et dolore magna aliqua. Ut enim ad minim veniam, quis nostrud exercitation ullamco laboris nisi ut aliquip ex ea commodo consequat. Duis aute irure dolor.</p>
    <div class="letter__closing">Yours Sincerely,</div>
    <span class="letter__signature" role="img" aria-label="Handwritten signature of the founder"></span>
  </div>

  <footer class="contact">
    <div class="contact__group">
      <div class="contact__line">
        <svg class="contact__icon" viewBox="0 0 10 10" aria-hidden="true"><path d="M2.2 0.6 L3.6 2.6 L2.8 3.6 C3.4 5 4.8 6.4 6.2 7 L7.2 6.2 L9.2 7.6 L8.4 9.2 C4.6 9 0.8 5.2 0.6 1.4 Z"/></svg>
        <span>(801) 555-0187</span>
      </div>
      <div class="contact__line">
        <svg class="contact__icon" viewBox="0 0 10 10" aria-hidden="true"><path d="M0.5 2 H9.5 V8.2 H0.5 Z M0.5 2 L5 5.6 L9.5 2" fill="none" stroke="#4b3234" stroke-width="1.1"/></svg>
        <span>brindlow.tile@mailbox.com</span>
      </div>
    </div>
    <div class="contact__group contact__group--end">
      <div class="contact__line">
        <span>www.brindlowtile.com</span>
        <svg class="contact__icon" viewBox="0 0 10 10" aria-hidden="true"><circle cx="5" cy="5" r="4.3" fill="none" stroke="#4b3234" stroke-width="1"/><path d="M0.7 5 H9.3 M5 0.7 C2.8 3 2.8 7 5 9.3 M5 0.7 C7.2 3 7.2 7 5 9.3" fill="none" stroke="#4b3234" stroke-width="0.8"/></svg>
      </div>
      <div class="contact__line">
        <span>Millbrook Utah, 84120</span>
        <svg class="contact__icon" viewBox="0 0 10 10" aria-hidden="true"><path d="M5 0.3 C2.8 0.3 1.4 1.9 1.4 3.8 C1.4 6.2 5 9.7 5 9.7 C5 9.7 8.6 6.2 8.6 3.8 C8.6 1.9 7.2 0.3 5 0.3 Z M5 2.4 A1.4 1.4 0 1 0 5 5.2 A1.4 1.4 0 1 0 5 2.4 Z" fill-rule="evenodd"/></svg>
      </div>
    </div>
  </footer>
</section>

<section class="envelope">
  <div class="envelope__flap"></div>
  <header class="company-name">
    <span class="company-name__square"></span>
    <span class="company-name__text">Brindlow Tile</span>
  </header>
</section>

</body>
</html>
```